K7 Electrical Services Ltd Web design

I require a web site for my new electrical contracting company. We are customer service orientated. Offering high value electrical installations, design and maintenance. Focused on custom residential and commercial upgrading. Lighting design and application are paramount in our company's services. Industry leading product use and integration are always on the forefront with our customer client services. As well as energy efficiency.

Target Market(s)

Homebuilders, General Contractors, Property management companies, clients, individuals,

Industry/Entity Type

Electric Company

Coding

Coded - Design and coding required

Number of Pages Required

3 page

Requirements
Must have
• Classic, modern, edgy but not trendy . Appeals to the masse.
• 3 page
• home page
• about page
• gallery page
• ability to contact from the webiste
Nice to have
• open to all types of designs that are relative to the construction industry.
• Black, Grey, metallic ice blue and deep purple colours from the logo.
Should not have
• anything cheesy with cartoon light bulb images.

```html
<!DOCTYPE html>
<html lang="en">
<head>
<meta charset="utf-8">
<title>K7 Electrical Services Ltd</title>
<link href="https://fonts.googleapis.com/css2?family=Ubuntu:wght@400;500;700&family=Roboto:ital,wght@0,400;0,500;1,400&display=swap" rel="stylesheet">
<style>
:root{
  --purple:#5b2a86;
  --purple-dark:#4a1f72;
  --yellow:#f6b700;
  --ink:#1a1a1a;
  --grey:#8a8a8a;
  --light:#f7f7f7;
  --white:#ffffff;
  --black:#0d0d0d;
}
*{box-sizing:border-box;margin:0;padding:0}
html,body{width:1200px;height:2568px;overflow:hidden;background:var(--white)}
body{font-family:"Roboto",sans-serif;color:var(--ink)}
.page{position:relative;width:1200px;height:2568px;overflow:hidden}
.abs{position:absolute}
.center{text-align:center}
.heading{font-family:"Ubuntu",sans-serif}

/* header */
.site-header{top:0;left:0;width:1200px;height:66px;background:var(--white)}
.brand{left:171px;top:18px;display:flex;align-items:center;gap:10px;font-family:"Ubuntu",sans-serif;font-weight:500;font-size:20px;color:var(--purple)}
.brand-dot{width:24px;height:24px;border-radius:50%;background:var(--purple)}
.main-nav{left:698px;top:25px;display:flex;gap:20px;font-family:"Ubuntu",sans-serif;font-size:13px;color:var(--ink)}
.main-nav .active{color:var(--purple)}
.header-social{left:934px;top:26px;display:flex;gap:15px}
.header-social span{width:11px;height:11px;border-radius:2px;background:var(--purple)}

/* hero */
.hero{top:66px;left:0;width:1200px;height:511px;background:linear-gradient(100deg,#3f4a5c 0%,#6b7584 40%,#9aa1a8 70%,#c9ccce 100%)}
.hero-shade{top:66px;left:0;width:1200px;height:511px;background:rgba(20,20,30,.35)}
.hero-rule{top:276px;left:340px;width:520px;height:1px;background:rgba(255,255,255,.6)}
.hero-kicker{top:294px;left:0;width:1200px;font-family:"Ubuntu",sans-serif;font-weight:500;font-size:18px;color:var(--white)}
.hero-title{top:318px;left:0;width:1200px;font-family:"Ubuntu",sans-serif;font-weight:500;font-size:42px;color:var(--white);letter-spacing:.5px}
.hero-text{top:372px;left:350px;width:500px;font-size:12.5px;line-height:17px;color:var(--white)}
.btn-outline{top:427px;left:517px;width:168px;height:38px;border:2px solid var(--white);border-radius:3px;color:var(--white);font-family:"Ubuntu",sans-serif;font-weight:500;font-size:15px;line-height:34px}

/* estimate */
.estimate{top:577px;left:0;width:1200px;height:109px;background:var(--purple)}
.estimate-title{top:595px;left:170px;font-family:"Ubuntu",sans-serif;font-weight:500;font-size:25px;color:var(--white)}
.estimate-text{top:628px;left:170px;width:250px;font-size:10.5px;line-height:12px;color:var(--white)}
.field{background:var(--white);font-size:11px;color:#777;padding:0 12px;line-height:38px;height:38px;border:1px solid #ddd}
.field-name{top:589px;left:483px;width:188px;background:#eeeeee}
.field-email{top:589px;left:680px;width:191px}
.field-phone{top:589px;left:878px;width:151px}
.field-msg{top:634px;left:483px;width:388px}
.btn-request{top:634px;left:878px;width:151px;height:38px;background:var(--yellow);color:var(--white);font-family:"Ubuntu",sans-serif;font-weight:500;font-size:12px;line-height:38px}
.pointer{top:686px;left:588px;width:0;height:0;border-left:12px solid transparent;border-right:12px solid transparent;border-top:12px solid var(--purple)}

/* services */
.section-title{font-family:"Ubuntu",sans-serif;font-weight:500;font-size:32px;color:var(--purple);left:0;width:1200px}
.services-title{top:742px}
.services-intro{top:786px;left:350px;width:500px;font-size:12.5px;line-height:17px;color:var(--ink)}
.service-ring{width:102px;height:102px;border-radius:50%;border:6px solid #f1f1f4;background:#f1f1f4;display:flex;align-items:center;justify-content:center;box-shadow:0 0 0 2px #fff inset}
.service-ring.featured{background:var(--purple);border-color:var(--purple)}
.service-ring svg{width:30px;height:30px}
.service-name{font-family:"Ubuntu",sans-serif;font-weight:500;font-size:14px;color:var(--purple);width:260px}
.service-desc{font-size:11.5px;line-height:17px;color:var(--grey);width:260px}

/* benefits */
.benefits{top:1096px;left:0;width:1200px;height:429px;background:var(--purple)}
.benefits-photo{top:1096px;left:410px;width:790px;height:429px;background:linear-gradient(90deg,rgba(91,42,134,0) 0%,rgba(140,110,170,.45) 60%,rgba(170,150,190,.5) 100%)}
.worker-figure{top:1150px;left:40px;width:270px;height:380px;background:linear-gradient(180deg,#e7b400 0%,#6a4a3a 30%,#2f7fd6 55%,#3a3a48 100%);border-radius:40px 40px 6px 6px}
.badge{top:1158px;left:552px;width:96px;height:96px;border-radius:50%;background:var(--white);color:var(--purple);font-family:"Ubuntu",sans-serif;font-weight:500;font-size:28px;line-height:96px}
.benefits-kicker{top:1272px;left:0;width:1200px;font-family:"Ubuntu",sans-serif;font-weight:500;font-size:23px;color:var(--white)}
.benefits-title{top:1300px;left:0;width:1200px;font-family:"Ubuntu",sans-serif;font-weight:500;font-size:42px;color:var(--white)}
.btn-join{top:1374px;left:515px;width:170px;height:36px;background:var(--yellow);color:var(--white);font-family:"Ubuntu",sans-serif;font-weight:500;font-size:14px;line-height:36px}

/* gallery */
.gallery{top:1525px;left:0;width:1200px;height:517px;display:grid;grid-template-columns:399px 404px 397px;grid-template-rows:258px 259px}
.tile{width:100%;height:100%}
.tile-1{background:linear-gradient(135deg,#8a6a4a,#3b5f9a)}
.tile-2{background:linear-gradient(135deg,#e4e4e4,#9a9a9a)}
.tile-3{background:linear-gradient(135deg,#f0c419,#6fa0d8 50%,#c8cdd3)}
.tile-4{background:linear-gradient(135deg,#a06a3a,#5a5a60 60%,#c99a5a)}
.tile-5{background:linear-gradient(135deg,#3a3f4a,#d97a2a 40%,#1f3a7a)}
.tile-6{background:linear-gradient(135deg,#0a1a4a,#2a6ae0 55%,#0a0f2a)}

/* reviews */
.reviews{top:2042px;left:0;width:1200px;height:348px;background:var(--light)}
.reviews-title{top:2080px}
.review-photo{top:2146px;left:245px;width:215px;height:200px;background:var(--white);padding:7px;box-shadow:0 1px 4px rgba(0,0,0,.15)}
.review-photo-fill{width:100%;height:100%;background:linear-gradient(160deg,#7a5a48 0%,#b48a70 45%,#d6336c 100%)}
.quote-mark{top:2280px;left:395px;font-family:"Ubuntu",sans-serif;font-weight:700;font-size:64px;line-height:64px;color:var(--white)}
.review-text{top:2138px;left:491px;width:451px;font-style:italic;font-size:13px;line-height:19px;color:#555}
.review-thanks{top:2246px;left:491px;font-style:italic;font-size:13px;font-weight:500;color:var(--ink)}
.review-name{top:2286px;left:491px;font-family:"Ubuntu",sans-serif;font-weight:500;font-size:14px;color:var(--purple)}
.review-place{top:2310px;left:491px;font-style:italic;font-size:10px;color:var(--ink)}
.arrow-btn{top:2201px;width:34px;height:34px;display:flex;align-items:center;justify-content:center}
.arrow-prev{left:134px;background:var(--black)}
.arrow-next{left:1026px;background:var(--purple)}

/* subscribe */
.subscribe{top:2390px;left:0;width:1200px;height:59px;background:var(--black)}
.subscribe-text{top:2405px;left:175px;font-family:"Ubuntu",sans-serif;font-size:22px;color:var(--white)}
.subscribe-text strong{font-weight:500}
.subscribe-input{top:2400px;left:587px;width:302px;height:38px;background:var(--white);font-size:10px;color:#888;padding:0 10px;line-height:38px}
.btn-subscribe{top:2400px;left:899px;width:125px;height:38px;background:var(--yellow);color:var(--white);font-family:"Ubuntu",sans-serif;font-weight:500;font-size:11px;line-height:38px}

/* footer */
.footer-social{top:2465px;left:546px;display:flex;gap:8px}
.footer-social span{width:27px;height:27px;border-radius:50%;background:#b5b5b5}
.footer-rule{top:2511px;left:235px;width:732px;height:1px;background:#e2e2e2}
.footer-nav{top:2530px;left:0;width:1200px;font-size:11.5px;color:#555}
.footer-nav span{margin:0 10px}
.copyright{top:2552px;left:0;width:1200px;font-size:9.5px;color:#555}
</style>
</head>
<body>
<div class="page">

  <header class="site-header abs">
    <div class="brand abs"><span class="brand-dot"></span>K7 Electrical Services</div>
    <nav class="main-nav abs"><span class="active">HOME</span><span>ABOUT US</span><span>GALLERY</span></nav>
    <div class="header-social abs"><span></span><span></span><span></span><span></span></div>
  </header>

  <section>
    <div class="hero abs" role="img" aria-label="Electrician in a yellow hard hat working on a distribution board"></div>
    <div class="hero-shade abs"></div>
    <div class="hero-rule abs"></div>
    <p class="hero-kicker abs center">OFFERING HIGH VALUE ELECTRICAL INSTALLATIONS</p>
    <h1 class="hero-title abs center">BEST ELECTRICAL SERVICES</h1>
    <p class="hero-text abs center">Lorem ipsum dolor sit amet, ultrices diam netus, at libero amet nulla. Vitae pulvinar, integer nec erat id lectus sit ligula, phasellus egestas</p>
    <div class="btn-outline abs center">MORE ABOUT US</div>
  </section>

  <section>
    <div class="estimate abs"></div>
    <h2 class="estimate-title abs">Request a Free Estimate</h2>
    <p class="estimate-text abs">Lorem ipsum dolor sit amet, consectetur adipiscing elit. Theophrasti igitur, inquit, tibi liber</p>
    <div class="field field-name abs">Name*</div>
    <div class="field field-email abs">Email Address*</div>
    <div class="field field-phone abs">Phone*</div>
    <div class="field field-msg abs">Your Message*</div>
    <div class="btn-request abs center">REQUEST NOW</div>
    <div class="pointer abs"></div>
  </section>

  <section>
    <h2 class="section-title services-title abs center">OUR SERVICES</h2>
    <p class="services-intro abs center">Lorem ipsum dolor sit amet, ultrices diam netus, at libero amet nulla. Vitae pulvinar, integer nec erat id lectus sit ligula, phasellus egestas</p>

    <svg class="abs" style="top:870px;left:330px" width="540" height="60" viewBox="0 0 540 60">
      <path d="M10 50 Q95 0 180 28" fill="none" stroke="#c9c9d2" stroke-width="1.5" stroke-dasharray="4 4"/>
      <path d="M174 22 L182 28 L173 33" fill="none" stroke="#c9c9d2" stroke-width="1.5"/>
      <path d="M360 10 Q445 -5 525 30" fill="none" stroke="#c9c9d2" stroke-width="1.5" stroke-dasharray="4 4"/>
      <path d="M518 22 L527 31 L516 34" fill="none" stroke="#c9c9d2" stroke-width="1.5"/>
    </svg>

    <div class="service-ring abs" style="top:859px;left:226px">
      <svg viewBox="0 0 30 30"><path d="M9 6 V11 M15 6 V11 M6 11 H18 V16 A6 6 0 0 1 6 16 Z M12 22 V25 Q12 27 16 27 H24" fill="none" stroke="#5b2a86" stroke-width="2" stroke-linecap="round"/></svg>
    </div>
    <div class="service-ring featured abs" style="top:859px;left:549px">
      <svg viewBox="0 0 30 30"><path d="M7 7 L23 23 M23 7 L7 23" stroke="#fff" stroke-width="3" stroke-linecap="round"/><circle cx="7" cy="7" r="3" fill="none" stroke="#fff" stroke-width="2"/><circle cx="23" cy="7" r="3" fill="none" stroke="#fff" stroke-width="2"/></svg>
    </div>
    <div class="service-ring abs" style="top:859px;left:870px">
      <svg viewBox="0 0 30 30"><rect x="8" y="8" width="14" height="14" rx="2" fill="none" stroke="#5b2a86" stroke-width="2"/><rect x="12" y="12" width="6" height="6" fill="#5b2a86"/><path d="M11 4 V8 M15 4 V8 M19 4 V8 M11 22 V26 M15 22 V26 M19 22 V26 M4 11 H8 M4 15 H8 M4 19 H8 M22 11 H26 M22 15 H26 M22 19 H26" stroke="#5b2a86" stroke-width="1.6"/></svg>
    </div>

    <h3 class="service-name abs center" style="top:964px;left:147px">ELECTRICAL SERVICES</h3>
    <p class="service-desc abs center" style="top:988px;left:147px">Lorem ipsum dolor sit amet, consectetuer adipiscing elit, sed diam nonummy nibh euismod Praesent interdum.</p>
    <h3 class="service-name abs center" style="top:964px;left:470px">ELECTRICAL SAFETY</h3>
    <p class="service-desc abs center" style="top:988px;left:470px">Lorem ipsum dolor sit amet, consectetuer adipiscing elit, sed diam nonummy nibh euismod Praesent interdum.</p>
    <h3 class="service-name abs center" style="top:964px;left:791px">CHANGE PANEL</h3>
    <p class="service-desc abs center" style="top:988px;left:791px">Lorem ipsum dolor sit amet, consectetuer adipiscing elit, sed diam nonummy nibh euismod Praesent interdum.</p>
  </section>

  <section>
    <div class="benefits abs"></div>
    <div class="benefits-photo abs" role="img" aria-label="Faded photo of an electrician working on a ladder"></div>
    <div class="badge abs center">K7</div>
    <p class="benefits-kicker abs center">FAST ELECTRICIAN SERVICES</p>
    <h2 class="benefits-title abs center">BENEFITS OF ELECTRICIAN</h2>
    <div class="btn-join abs center">JOIN US NOW</div>
  </section>

  <section class="gallery abs">
    <div class="tile tile-1" role="img" aria-label="Hands testing circuit breakers with a probe"></div>
    <div class="tile tile-2" role="img" aria-label="Finger switching a row of circuit breakers"></div>
    <div class="tile tile-3" role="img" aria-label="Electrician in a hard hat working at a panel"></div>
    <div class="tile tile-4" role="img" aria-label="Ceiling light fitting being installed"></div>
    <div class="tile tile-5" role="img" aria-label="Electrician in an orange hard hat on a ladder"></div>
    <div class="tile tile-6" role="img" aria-label="Blue LED ceiling lighting design"></div>
  </section>

  <div class="worker-figure abs" role="img" aria-label="Electrician holding a coil of blue cable"></div>

  <section>
    <div class="reviews abs"></div>
    <h2 class="section-title reviews-title abs center">OUR CUSTOMERS REVEIWS</h2>
    <div class="arrow-btn arrow-prev abs"><svg width="12" height="14" viewBox="0 0 12 14"><path d="M9 1 L3 7 L9 13" fill="none" stroke="#fff" stroke-width="2"/></svg></div>
    <div class="review-photo abs"><div class="review-photo-fill" role="img" aria-label="Portrait of the customer"></div></div>
    <div class="quote-mark abs">&#8220;</div>
    <p class="review-text abs">“Lorem ipsum dolor sit amet, consectetur adipiscing elit. Parvi enim primo ortu sic iacent, tamquam omnino sine animo sint. Est, ut dicis, inquit; Rhetorice igitur, inquam, nos mavis quam dialectice disputare? Quid, de quo nulla dissensio est? Bestiarum vero nullum iudicium puto. Duo Reges: constructio interrete.</p>
    <p class="review-thanks abs">Thank You so much for your design &amp; Expertise.”</p>
    <p class="review-name abs">MARIA LENTON</p>
    <p class="review-place abs">Apartment view, Lakeside</p>
    <div class="arrow-btn arrow-next abs"><svg width="12" height="14" viewBox="0 0 12 14"><path d="M3 1 L9 7 L3 13" fill="none" stroke="#fff" stroke-width="2"/></svg></div>
  </section>

  <section>
    <div class="subscribe abs"></div>
    <p class="subscribe-text abs"><strong>SUBSCRIBE NOW,</strong> AND JOIN THE FAMILY!</p>
    <div class="subscribe-input abs">Enter your email address</div>
    <div class="btn-subscribe abs center">SUBSCRIBE NOW</div>
  </section>

  <footer>
    <div class="footer-social abs"><span></span><span></span><span></span><span></span></div>
    <div class="footer-rule abs"></div>
    <p class="footer-nav abs center"><span>Home</span>|<span>About Us</span>|<span>Gallery</span>|<span>Contact Us</span></p>
    <p class="copyright abs center">© 2018 K7 Electrical. All rights reserved</p>
  </footer>

</div>
</body>
</html>
```